Quote Cards for Social Media RV

I would like to put these quotes over one of the pictures attached; One Quote per picture, and I want the quote to be bold or easy to read as well. I provided a few reference graphics that I really like as examples below. In very small letters at the bottom add @RVCarloweDaily

All of the pictures are attached; you can pick any photo and add one quote to it; but no stock photography

Target Market(s)

women trying to lose weight

Requirements
Must have
• quotes and pictures attached
Should not have
• no stock photography

```html
<!DOCTYPE html>
<html lang="en">
<head>
<meta charset="utf-8">
<title>Quote Cards – RV</title>
<link rel="stylesheet" href="https://fonts.googleapis.com/css2?family=Oswald:wght@400;500&family=Open+Sans:wght@800&display=swap">
<style>
  :root {
    --page: #ffffff;
    --ink-light: #ffffff;
    --ink-dark: #1c1a1a;
    --stage-deep: #2e2272;
    --stage-violet: #5a3fb0;
    --stage-pink: #b8307f;
    --room-grey: #9d9a97;
    --room-light: #e4e2de;
    --studio-beige: #ece4d8;
    --studio-tan: #c9a27e;
    --veil: rgba(255, 255, 255, 0.72);
    --band: rgba(28, 20, 60, 0.55);
  }
  * { margin: 0; padding: 0; box-sizing: border-box; }
  html, body { width: 1096px; height: 1200px; overflow: hidden; background: var(--page); }
  .canvas { position: relative; width: 1096px; height: 1200px; }

  .card { position: absolute; overflow: hidden; }
  .card-glp { left: 141px; top: 88px; width: 362px; height: 495px; }
  .card-overnight { left: 547px; top: 88px; width: 409px; height: 495px; }
  .card-natural { left: 141px; top: 616px; width: 362px; height: 496px; }
  .card-natural-bold { left: 570px; top: 616px; width: 362px; height: 496px; }

  .photo { position: absolute; inset: 0; }
  .photo-stage {
    background: linear-gradient(160deg, var(--stage-violet) 0%, var(--stage-pink) 50%, var(--stage-deep) 100%);
  }
  .photo-room {
    background: linear-gradient(90deg, #6b6d70 0%, var(--room-grey) 35%, var(--room-light) 75%, #d2cfcb 100%);
  }
  .photo-studio {
    background: linear-gradient(120deg, var(--studio-beige) 0%, #e2d3c1 55%, var(--studio-tan) 100%);
  }

  .band {
    position: absolute; left: 0; right: 0; bottom: 0; height: 190px;
    background: linear-gradient(transparent, var(--band) 30%, var(--band));
  }

  .quote {
    position: absolute;
    font-family: "Oswald", "Arial Narrow", sans-serif;
    font-weight: 400;
    text-transform: uppercase;
    letter-spacing: -0.5px;
    transform: scaleX(0.82);
    transform-origin: left top;
  }
  .handle {
    position: absolute;
    font-family: "Oswald", "Arial Narrow", sans-serif;
    font-size: 13px;
    font-weight: 500;
    letter-spacing: -0.2px;
  }

  .card-glp .quote {
    left: 29px; top: 287px; width: 400px;
    font-size: 31px; line-height: 32px; color: var(--ink-light);
  }
  .card-glp .handle { left: 29px; top: 458px; color: var(--ink-light); }

  .veil { position: absolute; left: 28px; top: 272px; width: 353px; height: 199px; background: var(--veil); }
  .card-overnight .quote {
    left: 28px; width: 353px; top: 280px; transform: none;
    font-size: 34px; line-height: 38px; color: var(--ink-dark); text-align: center;
    letter-spacing: -1.2px;
  }
  .card-overnight .quote span { display: inline-block; transform: scaleX(0.93); }
  .card-overnight .handle { left: 28px; width: 353px; top: 444px; text-align: center; color: var(--ink-dark); }

  .card-natural .quote {
    left: 28px; top: 240px; width: 220px;
    font-size: 31px; line-height: 31.5px; color: var(--ink-dark);
  }
  .card-natural .handle { left: 28px; top: 460px; color: var(--ink-dark); }

  .card-natural-bold .quote {
    left: 0; right: 0; top: 298px; transform: none;
    font-family: "Open Sans", Arial, sans-serif; font-weight: 800;
    font-size: 28px; line-height: 26.5px; letter-spacing: -1.4px;
    color: var(--ink-light); text-align: center;
    text-shadow: 0 1px 3px rgba(0,0,0,.55);
  }
  .card-natural-bold .handle {
    left: 0; right: 0; top: 430px; text-align: center; color: var(--ink-light);
    font-family: "Open Sans", Arial, sans-serif; font-weight: 800; font-size: 12px; letter-spacing: -0.4px;
  }
</style>
</head>
<body>
<main class="canvas">

  <article class="card card-glp">
    <div class="photo photo-stage" role="img" aria-label="Photo of RV in a pink gown on an awards stage"></div>
    <div class="band"></div>
    <p class="quote">GLP-1: The magic behind the<br>weight loss drugs. But<br>here's the secret - you can<br>boost it naturally without<br>a prescription!</p>
    <p class="handle">@RVCarloweDaily</p>
  </article>

  <article class="card card-overnight">
    <div class="photo photo-room" role="img" aria-label="Photo of RV in a sheer black striped top in a bright apartment"></div>
    <div class="veil"></div>
    <p class="quote"><span>Wake up tomorrow with<br>a flatter belly - yes, this<br>overnight remedy works<br>like magic!</span></p>
    <p class="handle">@RVCarloweDaily</p>
  </article>

  <article class="card card-natural">
    <div class="photo photo-studio" role="img" aria-label="Studio portrait of RV smiling in a tan turtleneck against a light wall"></div>
    <p class="quote">Finally-a<br>natural<br>solution that<br>flattens your<br>belly and eases<br>stomach bloat</p>
    <p class="handle">@RVCarloweDaily</p>
  </article>

  <article class="card card-natural-bold">
    <div class="photo photo-stage" role="img" aria-label="Photo of RV in a pink gown on an awards stage"></div>
    <div class="band"></div>
    <p class="quote">Finally-a natural<br>solution that<br>flattens your<br>belly and eases<br>stomach bloat</p>
    <p class="handle">@RVCarloweDaily</p>
  </article>

</main>
</body>
</html>
```